Business cards and logo for kitchen and bath remodeling company

We want an elegant card but that calls attention something unique and when people see it they remember us. A log that we can use for our own. We are a kitchen and bathroom remodeling company. We are 3 partners staring the company we are located in seattle washington usa. We try to give the best experience and luxury look in our projects and we are looking to show that in our cards. I added a sample of a card I really like. I like the black and gold look but gray blue or green in a metallic look would look nice. I'm open to any color.

Target Market(s)

Home owners.

Industry/Entity Type

Construction

Contact Information for Business Card

Larchmont and Vey builders

Colors

Designer to choose colors to be used in the design.

Requirements
Must have
• Make a Logo
• Logo to be unique
• Name of company larchmont and vey builders
Nice to have
• Have a good color scheme
• Front design to connect with back of card

```html
<!DOCTYPE html>
<html lang="en">
<head>
<meta charset="utf-8">
<title>Larchmont &amp; Vey Builders — Business Card</title>
<link href="https://fonts.googleapis.com/css2?family=Cinzel:wght@500&family=Work+Sans:wght@400;600&display=swap" rel="stylesheet">
<style>
  :root {
    --backdrop: #161616;
    --card: #1c1c1c;
    --card-edge: #262626;
    --gold: #c9a24a;
    --gold-soft: #b99340;
  }
  * { margin: 0; padding: 0; box-sizing: border-box; }
  html, body { width: 1200px; height: 900px; overflow: hidden; }
  body {
    background: var(--backdrop);
    font-family: "Work Sans", Arial, sans-serif;
    display: flex;
    flex-direction: column;
    align-items: center;
    justify-content: center;
    gap: 36px;
  }
  .card {
    width: 700px;
    height: 400px;
    background: linear-gradient(135deg, var(--card) 0%, var(--card-edge) 60%, var(--card) 100%);
    box-shadow: 0 12px 30px rgba(0,0,0,0.6);
    position: relative;
  }
  .brand {
    display: flex;
    align-items: center;
    gap: 14px;
    color: var(--gold);
    font-weight: 600;
  }
  .brand-mark {
    width: 22px;
    height: 22px;
    background: var(--gold);
    flex: none;
  }
  .brand-name { line-height: 1.1; }
  .brand-name span { display: block; }

  .card-front { display: flex; align-items: center; justify-content: center; }
  .card-front .brand-name { font-size: 38px; }
  .card-front .brand-name span:last-child { font-size: 26px; letter-spacing: 6px; }

  .card-back { display: flex; align-items: center; padding: 0 50px; }
  .card-back .brand { width: 300px; }
  .card-back .brand-name { font-size: 30px; }
  .card-back .brand-name span:last-child { font-size: 21px; letter-spacing: 5px; }
  .divider { width: 2px; height: 190px; background: var(--gold-soft); margin: 0 34px; }

  .contact { color: var(--gold); }
  .contact-name { font-family: "Cinzel", Georgia, serif; font-size: 26px; letter-spacing: 1px; }
  .contact-role { font-size: 16px; margin-bottom: 16px; }
  .contact-address { font-size: 17px; line-height: 1.35; margin-bottom: 12px; }
  .contact-list { list-style: none; font-size: 17px; line-height: 1.6; }
  .contact-list li { display: flex; align-items: center; gap: 10px; }
  .contact-list svg { width: 14px; height: 14px; fill: none; stroke: var(--gold); stroke-width: 1.6; }
</style>
</head>
<body>
  <section class="card card-front">
    <div class="brand">
      <div class="brand-mark"></div>
      <div class="brand-name"><span>Larchmont &amp; Vey</span><span>BUILDERS</span></div>
    </div>
  </section>

  <section class="card card-back">
    <div class="brand">
      <div class="brand-mark"></div>
      <div class="brand-name"><span>Larchmont &amp; Vey</span><span>BUILDERS</span></div>
    </div>
    <div class="divider"></div>
    <div class="contact">
      <p class="contact-name">DANIEL HARROW</p>
      <p class="contact-role">Director</p>
      <p class="contact-address">214 Cedar Ave.<br>Brookhaven, WA 98120</p>
      <ul class="contact-list">
        <li><svg viewBox="0 0 16 16"><path d="M4 1.5l2.5 3-1.5 1.5c.8 2 2.5 3.7 4.5 4.5L11 9l3 2.5-1.5 2.5C7 14 2 9 2 3z"/></svg>555-014-2270</li>
        <li><svg viewBox="0 0 16 16"><rect x="1.5" y="3.5" width="13" height="9"/><path d="M1.5 3.5L8 9l6.5-5.5"/></svg>info@larchmontvey.com</li>
        <li><svg viewBox="0 0 16 16"><circle cx="8" cy="8" r="6.5"/><path d="M1.5 8h13M8 1.5c-3 3.5-3 9.5 0 13M8 1.5c3 3.5 3 9.5 0 13"/></svg>www.larchmontvey.com</li>
      </ul>
    </div>
  </section>
</body>
</html>
```